Business car for dental practice

I have a new logo. Want it use for a new business card design. Hi end dental practice Would like a scan code on it for quick access to my web site and mobile site too. Green and purple are in logo design. Maybe have scan code on back? My website is peterhalvorsenDDS.example
Updates

Lakemont Crest Dental Associates

248 N Fairlawn Ave
Harlow Bend, NY 10988
555-318-4072

317 N Wexford Rd. 
Suite 406
Elm Ridge, NY 10977
555-762-1938

would like to incorporate logo, and addresses of both offices, and I recently saw a business card with a scan box on it which would bring people directly to the web site. if anyone knows how to do that, that could possibly go on the back of the card. (May be something I have to add at printing process) card can be one sided, or two sided.  

Reason: designer is revising for me. has not posted changes yet. hope he does soon!!

Industry/Entity Type

Business

```html
<!DOCTYPE html>
<html lang="en">
<head>
<meta charset="utf-8">
<title>Lakemont Crest Dental Associates – Business Card</title>
<link rel="stylesheet" href="https://fonts.googleapis.com/css2?family=Libre+Baskerville:wght@400&family=Arimo:wght@400&display=swap">
<style>
  :root {
    --purple: #6e1f57;
    --purple-dark: #4e1440;
    --purple-light: #8a2a6e;
    --green: #519c45;
    --pink-rule: #c2407f;
    --paper: #ffffff;
    --ink: #1d1d1d;
    --stage: #e7e5e2;
  }
  * { margin: 0; padding: 0; box-sizing: border-box; }
  html, body { width: 1200px; height: 900px; overflow: hidden; background: var(--stage); }
  .canvas { position: relative; width: 1200px; height: 900px; }

  .card {
    position: absolute;
    width: 656px;
    height: 376px;
    background: var(--paper);
    overflow: hidden;
    box-shadow: 0 2px 8px rgba(0,0,0,.25);
  }
  .card--front { left: 30px; top: 51px; }
  .card--back  { left: 426px; top: 448px; }

  .bar {
    position: absolute;
    background: linear-gradient(90deg, var(--purple-light), var(--purple) 60%, var(--purple-dark));
    box-shadow: 2px 0 4px rgba(0,0,0,.3);
  }

  .rule { position: absolute; height: 1px; background: var(--pink-rule); }
  .band-green { position: absolute; left: 0; right: 0; background: var(--green); }
  .band-purple { position: absolute; left: 0; right: 0; background: var(--purple); }

  .brand { position: absolute; display: flex; align-items: center; gap: 4px; }
  .brand__mark { width: 70px; height: 70px; background: var(--purple); flex: none; }
  .brand__name {
    font-family: "Libre Baskerville", Georgia, serif;
    font-weight: 400;
    color: var(--purple);
    line-height: 1;
    white-space: nowrap;
  }
  .brand__line1 { display: block; font-size: 38px; }
  .brand__line2 { display: block; font-size: 17px; letter-spacing: 4.5px; margin-top: 4px; padding-left: 38px; }

  .contacts { position: absolute; left: 263px; top: 222px; list-style: none; }
  .contacts li {
    display: flex; align-items: center; gap: 11px;
    height: 22px; margin-bottom: 4px;
    font-family: "Arimo", Arial, sans-serif; font-size: 15px; color: var(--ink);
    white-space: nowrap;
  }
  .contacts li:nth-child(2) { margin-bottom: 3px; }
  .icon { width: 22px; height: 22px; background: var(--purple); display: flex; align-items: center; justify-content: center; flex: none; }
</style>
</head>
<body>
<div class="canvas">

  <section class="card card--front" aria-label="Card front">
    <div class="bar" style="left:130px; top:0; width:32px; height:62px;"></div>
    <div class="bar" style="left:170px; top:0; width:30px; height:62px;"></div>

    <div class="brand" style="left:130px; top:146px;">
      <div class="brand__mark"></div>
      <div class="brand__name">
        <span class="brand__line1">Lakemont Crest</span>
        <span class="brand__line2">Dental Associates</span>
      </div>
    </div>

    <div class="rule" style="left:0; width:130px; top:234px;"></div>
    <div class="rule" style="left:200px; right:0; top:234px;"></div>

    <div class="band-green" style="top:266px; bottom:0;"></div>
    <div class="bar" style="left:130px; top:266px; width:32px; bottom:0;"></div>
    <div class="bar" style="left:170px; top:266px; width:30px; bottom:0;"></div>
  </section>

  <section class="card card--back" aria-label="Card back">
    <div class="band-green" style="top:0; height:108px;"></div>
    <div class="bar" style="left:26px; top:0; width:32px; height:108px;"></div>
    <div class="bar" style="left:65px; top:0; width:30px; height:108px;"></div>

    <div class="brand" style="left:26px; top:122px;">
      <div class="brand__mark"></div>
      <div class="brand__name">
        <span class="brand__line1">Lakemont Crest</span>
        <span class="brand__line2">Dental Associates</span>
      </div>
    </div>

    <ul class="contacts">
      <li>
        <span class="icon"><svg width="12" height="16" viewBox="0 0 12 16" aria-hidden="true"><path d="M6 0a6 6 0 0 0-6 6c0 4.5 6 10 6 10s6-5.5 6-10a6 6 0 0 0-6-6zm0 8.5A2.5 2.5 0 1 1 6 3.5a2.5 2.5 0 0 1 0 5z" fill="#519c45"/></svg></span>
        248 N Fairlawn Ave, Harlow Bend, NY 10988
      </li>
      <li>
        <span class="icon"><svg width="16" height="12" viewBox="0 0 16 12" aria-hidden="true"><path d="M1 3c0-2 3-3 7-3s7 1 7 3v1h-4V3H5v1H1zM3 5h10l2 7H1z" fill="#519c45"/><circle cx="8" cy="8.5" r="2" fill="#6e1f57"/></svg></span>
        555 - 318 - 4072
      </li>
      <li>
        <span class="icon"><svg width="12" height="16" viewBox="0 0 12 16" aria-hidden="true"><path d="M6 0a6 6 0 0 0-6 6c0 4.5 6 10 6 10s6-5.5 6-10a6 6 0 0 0-6-6zm0 8.5A2.5 2.5 0 1 1 6 3.5a2.5 2.5 0 0 1 0 5z" fill="#519c45"/></svg></span>
        317 N Wexford Rd. Suite 406 Elm Ridge, NY 10977
      </li>
      <li>
        <span class="icon"><svg width="16" height="12" viewBox="0 0 16 12" aria-hidden="true"><path d="M1 3c0-2 3-3 7-3s7 1 7 3v1h-4V3H5v1H1zM3 5h10l2 7H1z" fill="#519c45"/><circle cx="8" cy="8.5" r="2" fill="#6e1f57"/></svg></span>
        555-762-1938
      </li>
    </ul>

    <div class="band-purple" style="top:358px; bottom:0;"></div>
    <div class="bar" style="left:26px; top:312px; width:32px; bottom:0;"></div>
    <div class="bar" style="left:65px; top:312px; width:30px; bottom:0;"></div>
  </section>

</div>
</body>
</html>
```